Phone Repair Business Card

I need a business card for my mobile phone/ smart phone and tablet repair business based in New Zealand. My business name is "T.K. Repairs". I would like to see a designer make a modern phone related business card, which could incorporate something to do with the Zorvel Kavlo as this is our main repaired product. i like the dark Grey and lime green colours

```html
<!DOCTYPE html>
<html lang="en">
<head>
<meta charset="utf-8">
<title>T.K. Repairs – Business Card</title>
<link rel="stylesheet" href="https://fonts.googleapis.com/css2?family=Michroma&display=swap">
<style>
  :root {
    --backdrop-light: #f2f2f2;
    --backdrop-dark: #cfcfcf;
    --card-surface: #d5d2cc;
    --ink-dark: #2a2a2a;
    --ink-mid: #3a3a3a;
    --lime: #7cbf1e;
    --divider: #2e2e2e;
  }
  html, body {
    margin: 0;
    width: 1200px;
    height: 750px;
    overflow: hidden;
  }
  body {
    background: radial-gradient(ellipse at 40% 30%, var(--backdrop-light), var(--backdrop-dark));
    font-family: "Michroma", sans-serif;
    color: var(--ink-dark);
  }
  .business-card {
    position: absolute;
    left: 180px;
    top: 135px;
    width: 840px;
    height: 480px;
    background: var(--card-surface);
    box-shadow: 0 10px 30px rgba(0,0,0,0.18);
  }
  .brand {
    position: absolute;
    left: 150px;
    top: 78px;
    width: 560px;
  }
  .brand-line {
    display: flex;
    align-items: center;
    gap: 14px;
    padding-left: 40px;
  }
  .brand-mark {
    width: 22px;
    height: 22px;
    background: var(--lime);
    flex: none;
  }
  .brand-name {
    margin: 0;
    font-size: 34px;
    font-weight: 400;
    color: var(--ink-dark);
    line-height: 1.1;
    white-space: nowrap;
  }
  .brand-tagline {
    margin: 14px 0 0;
    font-size: 14px;
    color: var(--ink-mid);
    white-space: nowrap;
  }
  .person {
    position: absolute;
    left: 130px;
    top: 290px;
  }
  .person-name {
    margin: 0;
    font-size: 22px;
    font-weight: 400;
    color: var(--ink-mid);
    white-space: nowrap;
  }
  .person-role {
    margin: 6px 0 0;
    font-size: 13px;
    color: var(--lime);
  }
  .divider {
    position: absolute;
    left: 470px;
    top: 200px;
    width: 2px;
    height: 140px;
    background: var(--divider);
  }
  .contact-list {
    position: absolute;
    left: 500px;
    top: 196px;
    margin: 0;
    padding: 0;
    list-style: none;
    font-size: 13px;
    color: var(--ink-mid);
  }
  .contact-item {
    display: flex;
    align-items: center;
    gap: 10px;
    height: 28px;
    white-space: nowrap;
  }
  .contact-icon {
    width: 18px;
    height: 18px;
    flex: none;
  }
</style>
</head>
<body>
  <main class="business-card">
    <header class="brand">
      <div class="brand-line">
        <span class="brand-mark" aria-hidden="true"></span>
        <h1 class="brand-name">T.K. Repairs</h1>
      </div>
      <p class="brand-tagline">mobile phone/smart phone and tablet repair</p>
    </header>

    <section class="person">
      <h2 class="person-name">Your Name</h2>
      <p class="person-role">director</p>
    </section>

    <div class="divider"></div>

    <ul class="contact-list">
      <li class="contact-item">
        <svg class="contact-icon" viewBox="0 0 18 18" aria-hidden="true">
          <circle cx="9" cy="9" r="9" fill="var(--lime)"/>
          <rect x="6" y="3.5" width="6" height="11" rx="1.2" fill="none" stroke="#fff" stroke-width="1.4"/>
          <circle cx="9" cy="12.3" r="0.8" fill="#fff"/>
        </svg>
        <span>0123456789</span>
      </li>
      <li class="contact-item">
        <svg class="contact-icon" viewBox="0 0 18 18" aria-hidden="true">
          <circle cx="9" cy="9" r="9" fill="var(--lime)"/>
          <rect x="4" y="5.5" width="10" height="7" fill="none" stroke="#fff" stroke-width="1.3"/>
          <polyline points="4,5.5 9,9.8 14,5.5" fill="none" stroke="#fff" stroke-width="1.3"/>
        </svg>
        <span>yourname@tkrepairs.nz</span>
      </li>
      <li class="contact-item">
        <svg class="contact-icon" viewBox="0 0 18 18" aria-hidden="true">
          <circle cx="9" cy="9" r="9" fill="var(--lime)"/>
          <circle cx="9" cy="9" r="5" fill="none" stroke="#fff" stroke-width="1.2"/>
          <ellipse cx="9" cy="9" rx="2.2" ry="5" fill="none" stroke="#fff" stroke-width="1.1"/>
          <line x1="4" y1="9" x2="14" y2="9" stroke="#fff" stroke-width="1.1"/>
        </svg>
        <span>www.tkrepairs.nz</span>
      </li>
    </ul>
  </main>
</body>
</html>
```